Consultant Firm Marketing Flyer

I want to use this flyer to market health care consultant services. I would like a front and back glossy, professional, yet bold and eye catching design. I would like it to convey knowledge, expertise, partnership and strength. The colors should blue and white but I am very open to the designer being creative. You can visit my website to see colors and images I want to use at brightharborcare.net
I would like the home page image on my website to be incorporated into the flyer but I am also open to other images that work with the design. The designer can be creative.

I want to highlight 4 service area’s of focus to my clients:
1. Revenue Cycle Optimization (making my clients money)
2. Practice Management Optimization (improving clinical operations)
3. Health Compliance (following the law)
4. Health Care Technology: (Telemedicine and AI)
Please be creative. Go where ever your creativity leads.

```html
<!DOCTYPE html>
<html lang="en">
<head>
<meta charset="utf-8">
<title>Bright Harbor Care Solutions – Flyer</title>
<link rel="stylesheet" href="https://fonts.googleapis.com/css2?family=Montserrat:wght@500;600;800&family=Open+Sans:wght@400&family=Roboto+Condensed:wght@300&display=swap">
<style>
  :root {
    --bg: #e4e4e4;
    --paper: #ffffff;
    --brand-blue: #3d8fd6;
    --deep-blue: #2c62b8;
    --mid-blue: #5e9ee6;
    --light-blue: #b9dcf7;
    --pale-blue: #dcefff;
    --ink: #555a63;
    --title-ink: #2e4a78;
    --icon-ink: #2a4c9c;
    --tile-1a: #bcd9f6;
    --tile-1b: #8ec3ef;
    --tile-2: #9dcff0;
    --tile-3: #c8cbd0;
    --tile-4: #f4f5f7;
    --footer-a: #3846ab;
    --footer-b: #1676c8;
    --white: #ffffff;
  }
  * { box-sizing: border-box; margin: 0; padding: 0; }
  html, body { width: 1200px; height: 900px; overflow: hidden; background: var(--bg); }
  .flyer {
    position: absolute; left: 268px; top: 20px;
    width: 664px; height: 860px;
    background: var(--paper); overflow: hidden;
  }
  .brand {
    position: absolute; left: 32px; top: 52px;
    font-family: "Montserrat", sans-serif; font-weight: 500;
    font-size: 11px; letter-spacing: 0.4px; color: var(--brand-blue);
  }
  .brand-mark {
    position: absolute; left: 32px; top: 44px;
    width: 10px; height: 10px; border-radius: 50%; background: var(--brand-blue);
    display: none;
  }
  .hero { position: absolute; left: 0; top: 0; width: 664px; height: 441px; }
  .headline {
    position: absolute; right: 28px; top: 283px; text-align: right;
    font-family: "Montserrat", sans-serif; font-weight: 800; color: var(--white);
    line-height: 1; text-transform: uppercase;
  }
  .headline .lead { display: block; font-size: 25px; letter-spacing: 0.3px; }
  .headline .main { display: block; font-size: 34px; margin-top: 2px; letter-spacing: 0.2px; }
  .intro {
    position: absolute; left: 26px; top: 472px; width: 610px;
    font-family: "Roboto Condensed", sans-serif; font-weight: 300;
    font-size: 14.2px; line-height: 18.5px; color: var(--ink);
  }
  .services {
    position: absolute; left: 0; top: 598px; width: 664px; height: 173px;
    display: flex;
  }
  .service {
    flex: 0 0 auto; height: 100%; text-align: center;
    padding-top: 21px;
  }
  .service:nth-child(1) { width: 165px; background: linear-gradient(135deg, var(--tile-1a), var(--tile-1b)); }
  .service:nth-child(2) { width: 168px; background: var(--tile-2); }
  .service:nth-child(3) { width: 168px; background: var(--tile-3); }
  .service:nth-child(4) { width: 163px; background: var(--tile-4); }
  .service-icon { width: 44px; height: 44px; display: block; margin: 0 auto; }
  .service-title {
    font-family: "Montserrat", sans-serif; font-weight: 500; font-size: 13px;
    line-height: 16px; color: var(--title-ink); text-transform: uppercase;
    margin-top: 18px; height: 48px; letter-spacing: 0.3px;
  }
  .service-note {
    font-family: "Open Sans", sans-serif; font-size: 11px; color: #3e4450;
  }
  .service:nth-child(1) .service-note { margin-top: -17px; }
  .footer {
    position: absolute; left: 0; top: 771px; width: 664px; height: 89px;
    background: linear-gradient(100deg, var(--footer-a), var(--footer-b));
    display: flex; align-items: center; padding-left: 32px;
    font-family: "Open Sans", sans-serif; font-size: 11px; line-height: 14.5px; color: var(--white);
  }
  .contact { display: flex; align-items: center; gap: 16px; }
  .contact svg { width: 28px; height: 28px; flex: none; }
  .contact-address { width: 200px; }
  .contact-phone { width: 146px; margin-left: 16px; }
  .contact-phone span { align-self: flex-start; margin-top: 0; }
  .contact-web { margin-left: 4px; }
</style>
</head>
<body>
<main class="flyer">

  <svg class="hero" viewBox="0 0 664 441" aria-hidden="false">
    <defs>
      <linearGradient id="photoTone" x1="0" y1="0" x2="1" y2="1">
        <stop offset="0" stop-color="#c9d2da"/>
        <stop offset="0.45" stop-color="#9fb2c6"/>
        <stop offset="1" stop-color="#6f8fb6"/>
      </linearGradient>
      <linearGradient id="veil" x1="0" y1="0" x2="1" y2="0">
        <stop offset="0" stop-color="#9fd0f5" stop-opacity="0.35"/>
        <stop offset="1" stop-color="#6fb3f0" stop-opacity="0.85"/>
      </linearGradient>
    </defs>

    <!-- top right diagonal ribbons -->
    <polygon points="440,0 664,0 664,62 398,62" fill="#e6f5ff"/>
    <polygon points="525,0 600,0 560,62 490,62" fill="#cdebff"/>
    <polygon points="610,0 664,0 664,62 580,62" fill="#b5dbf8"/>
    <polygon points="410,62 584,62 539,137 360,137" fill="#b7d9f7"/>
    <polygon points="584,62 664,62 664,137 539,137" fill="var(--deep-blue)"/>

    <!-- photograph area -->
    <polygon role="img" aria-label="Photo of four healthcare professionals meeting around a table in a bright office"
      points="0,137 664,137 664,366 568,366 524,441 26,441 114,289 0,289" fill="url(#photoTone)"/>

    <!-- blue overlays across the photo -->
    <polygon points="40,137 123,137 70,212 0,212 0,195" fill="var(--mid-blue)" opacity="0.8"/>
    <polygon points="470,137 664,137 664,366 600,366 560,366 412,366" fill="url(#veil)"/>
    <polygon points="114,289 180,289 92,441 26,441" fill="#a9d3f6" opacity="0.75"/>
    <polygon points="210,366 568,366 524,441 170,441" fill="var(--deep-blue)" opacity="0.55"/>
    <polygon points="470,366 568,366 524,441 430,441" fill="var(--deep-blue)" opacity="0.75"/>
    <polygon points="0,137 140,137 0,330" fill="#ffffff" opacity="0.12"/>
  </svg>

  <div class="brand">Bright Harbor Care Solutions LLC</div>

  <h1 class="headline">
    <span class="lead">Advancing</span>
    <span class="main">Healthcare Operations</span>
  </h1>

  <p class="intro">Bright Harbor Care Solutions (BHC) is a healthcare consulting firm skilled at helping physician practices advance their strategic vision in an ever-evolving healthcare system. Bright Harbor Care Solutions specializes in revenue cycle optimization, practice management improvement and developing new physician practices. Our technical skills allow us to dig deep into your revenue cycle while our strategic approach ensures we’re keeping our eyes on the entire financial picture.</p>

  <section class="services">
    <article class="service">
      <svg class="service-icon" viewBox="0 0 44 44" fill="none" stroke="var(--icon-ink)" stroke-width="1.6">
        <rect x="2" y="24" width="5" height="12"/>
        <rect x="9" y="18" width="5" height="18"/>
        <rect x="16" y="12" width="5" height="14"/>
        <rect x="23" y="6" width="5" height="10"/>
        <circle cx="30" cy="30" r="11"/>
        <path d="M33.5 25.5c-1-1.2-6-1.8-6 1.2s6 2 6 5.2-5 2.6-6.5 1.2M30 22.5v15"/>
      </svg>
      <h2 class="service-title">Revenue Cycle<br>Optimization</h2>
      <p class="service-note">Making my clients money</p>
    </article>
    <article class="service">
      <svg class="service-icon" viewBox="0 0 44 44" fill="none" stroke="var(--icon-ink)" stroke-width="1.6">
        <circle cx="22" cy="22" r="20"/>
        <circle cx="22" cy="22" r="16.5"/>
        <path d="M22 8v28M14 13c4 -3 12 -3 16 0M17 18c4 3 6 3 10 0M17 24c4 -3 6 -3 10 0M18 29c3 2 5 2 8 0"/>
      </svg>
      <h2 class="service-title">Practice<br>Management<br>Optimization</h2>
      <p class="service-note">Improving clinical operations</p>
    </article>
    <article class="service">
      <svg class="service-icon" viewBox="0 0 44 44" fill="none" stroke="var(--icon-ink)" stroke-width="1.6">
        <circle cx="22" cy="22" r="20"/>
        <rect x="9" y="8" width="20" height="28" rx="1.5"/>
        <path d="M13 15h12M13 20h12M13 25h8M13 30h6"/>
        <circle cx="31" cy="27" r="8" fill="var(--tile-3)"/>
        <path d="M27 27l3 3 5-6"/>
      </svg>
      <h2 class="service-title">Health<br>Compliance</h2>
      <p class="service-note">Following the law</p>
    </article>
    <article class="service">
      <svg class="service-icon" viewBox="0 0 44 44" fill="none" stroke="var(--icon-ink)" stroke-width="1.6">
        <circle cx="22" cy="22" r="20"/>
        <circle cx="22" cy="22" r="16.5"/>
        <path d="M22 8v28M17 10v8l-5 4v6M27 10v8l5 4v6M17 22l3 3v8M27 22l-3 3v8"/>
        <circle cx="12" cy="29" r="1.6"/><circle cx="32" cy="29" r="1.6"/>
        <circle cx="17" cy="10" r="1.6"/><circle cx="27" cy="10" r="1.6"/>
      </svg>
      <h2 class="service-title">Health Care<br>Technology</h2>
      <p class="service-note">Telemedicine and AI</p>
    </article>
  </section>

  <footer class="footer">
    <div class="contact contact-address">
      <svg viewBox="0 0 28 28" fill="none" stroke="#ffffff" stroke-width="1.4">
        <path d="M3 14L14 4l11 10M6 11v14h6v-7h4v7h6V11M19 6v-2h3v5"/>
      </svg>
      <span>118 Linden Street Portland,<br>Maine Suite 310</span>
    </div>
    <div class="contact contact-phone">
      <svg viewBox="0 0 28 28" fill="none" stroke="#ffffff" stroke-width="1.4">
        <path d="M6 3l4 1 2 6-3 2c1.5 3.5 4 6 7 7.5l2-3 6 2 1 4c-1 2.5-3 3.5-5 3C11 24 4 17 3 8c-.3-2 1-4 3-5z"/>
      </svg>
      <span>555-014-2270</span>
    </div>
    <div class="contact contact-web">
      <svg viewBox="0 0 28 28" fill="none" stroke="#ffffff" stroke-width="1.4">
        <rect x="12" y="3" width="8" height="14" rx="4" transform="rotate(45 16 10)"/>
        <rect x="8" y="11" width="8" height="14" rx="4" transform="rotate(45 12 18)"/>
      </svg>
      <span>www.brightharborcare.net<br>info@brightharborcare.net</span>
    </div>
  </footer>

</main>
</body>
</html>
```